Visitenkarten-Design für Rohrreinigungsfirma
Zielgruppe
Wir sind eine Kanal.-Rohrreinigungsfirma und suchen ein hochwertiges Design, unsere Zielgruppe sind Firmenkunden,Hausverwaltungen, Architekten sowie Behörden.
Aufgabenstellung
Das Design sollte Edel aussehen. Es sollten unsere Dienstleistungen mit auf der Visitenkarte stehen (gerne auch Rückseite): grabenlose Kanalsanierung, TV-Kamerainspektion,Dichtheitsprüfung DIN EN 1610, Fräsarbeiten mit Roboter, Fräsarbeiten mit Wasserhöchstdruck 2.500 Bar,Verstopfungsbeseitigung. (Vorderseite sollte enthalten:

```html
<!DOCTYPE html>
<html lang="de">
<head>
<meta charset="utf-8">
<title>KRW Visitenkarte</title>
<link href="https://fonts.googleapis.com/css2?family=Montserrat:wght@500;600;700&display=swap" rel="stylesheet">
<style>
  :root {
    --blue: #3f5f86;
    --navy: #2a3a53;
    --red: #c0262c;
    --white: #ffffff;
    --ink: #2f4a6e;
    --label: #2b3648;
    --page: #ffffff;
  }
  * { margin: 0; padding: 0; box-sizing: border-box; }
  html, body { width: 1117px; height: 1200px; overflow: hidden; background: var(--page); }
  body { position: relative; font-family: "Montserrat", Arial, sans-serif; color: var(--ink); }

  .side-label { position: absolute; font-size: 24px; font-weight: 600; color: var(--label); }
  .side-label--front { left: 41px; top: 24px; }
  .side-label--back { left: 72px; top: 468px; }

  .card {
    position: absolute; width: 460px; height: 295px; overflow: hidden;
    background: var(--white); box-shadow: 0 1px 4px rgba(0,0,0,.25);
  }
  .card--front { left: 68px; top: 93px; }
  .card--back { left: 72px; top: 552px; }
  .card__bg { position: absolute; inset: 0; }

  .benefits { position: absolute; left: 18px; top: 30px; list-style: none; color: var(--white); font-size: 11.5px; font-weight: 500; line-height: 1.3; }
  .benefits li { position: relative; padding-left: 22px; margin-bottom: 7px; }
  .benefits li::before { content: "✓"; position: absolute; left: 0; top: -2px; font-size: 15px; font-weight: 700; }

  .services { position: absolute; left: 20px; top: 22px; list-style: none; color: var(--white); font-size: 13px; font-weight: 500; line-height: 1.35; }
  .services li { position: relative; padding-left: 16px; margin-bottom: 9px; }
  .services li::before { content: ""; position: absolute; left: 0; top: 7px; width: 5px; height: 5px; border-radius: 50%; background: var(--white); }

  .hotline { position: absolute; color: var(--white); font-weight: 700; text-align: center; }
  .card--front .hotline { left: 10px; top: 208px; font-size: 17px; line-height: 1.2; }
  .card--back .hotline { left: 17px; top: 216px; font-size: 15px; line-height: 1.2; }
  .hotline__icon { position: absolute; }

  .brand { position: absolute; left: 212px; top: 26px; }
  .brand__name { display: flex; align-items: center; gap: 10px; font-size: 30px; font-weight: 700; color: var(--ink); line-height: 1; }
  .brand__dot { width: 12px; height: 12px; border-radius: 50%; background: var(--ink); }
  .brand__trade { margin-top: 6px; font-size: 14.5px; font-weight: 700; color: var(--navy); letter-spacing: .2px; }
  .brand__claim { margin-top: 2px; margin-left: 40px; font-size: 10px; font-weight: 600; color: var(--red); }

  .contact { position: absolute; left: 258px; top: 107px; font-size: 12.5px; font-weight: 500; color: var(--ink); line-height: 1.45; }
  .contact__name { font-weight: 600; }
  .contact__phone { display: flex; align-items: center; gap: 6px; margin-top: 12px; }
  .contact__address { margin-top: 12px; }

  .footer-link { position: absolute; right: 24px; color: var(--white); font-size: 12.5px; font-weight: 500; }
  .card--front .footer-link { top: 257px; }
  .card--back .footer-link { top: 262px; font-size: 13px; }

  .callout { position: absolute; left: 288px; top: 50px; width: 160px; text-align: center; font-size: 16px; font-weight: 600; color: var(--navy); line-height: 1.4; }
  .callout p + p { margin-top: 16px; }
</style>
</head>
<body>
  <div class="side-label side-label--front">Vorderseite</div>

  <section class="card card--front" aria-label="Visitenkarte Vorderseite">
    <svg class="card__bg" viewBox="0 0 460 295" width="460" height="295" aria-hidden="true">
      <polygon points="0,0 152,0 250,295 0,295" fill="var(--blue)"/>
      <rect x="0" y="236" width="460" height="59" fill="var(--navy)"/>
      <path d="M0,206 H204 a34,34 0 0 1 0,68 H0 Z" fill="var(--red)"/>
    </svg>

    <ul class="benefits">
      <li>transparente<br>Preise</li>
      <li>moderne<br>Ausrüstung</li>
      <li>regionales<br>Unternehmen</li>
      <li>schnell &amp; zuverlässiger<br>Service</li>
    </ul>

    <div class="hotline">24H NOTDIENST<br>Tag &amp; Nacht<br>0150 - 000 111 22</div>
    <svg class="hotline__icon" style="left:168px;top:214px" width="52" height="54" viewBox="0 0 52 54" aria-hidden="true">
      <circle cx="30" cy="22" r="17" fill="none" stroke="#fff" stroke-width="3"/>
      <path d="M30 12 V22 L37 27" fill="none" stroke="#fff" stroke-width="3" stroke-linecap="round"/>
      <rect x="2" y="36" width="24" height="12" rx="2" fill="#fff"/>
      <circle cx="8" cy="50" r="3" fill="#fff"/><circle cx="21" cy="50" r="3" fill="#fff"/>
    </svg>

    <div class="brand">
      <div class="brand__name">KRW <span class="brand__dot"></span></div>
      <div class="brand__trade">KANAL- &amp; ROHRREINIGUNG</div>
      <div class="brand__claim">24 STUNDEN NOTDIENST</div>
    </div>

    <div class="contact">
      <div class="contact__name">LUKAS BERGER</div>
      <div>Geschäftsführer</div>
      <div class="contact__phone">
        <svg width="12" height="12" viewBox="0 0 24 24" aria-hidden="true"><path fill="var(--ink)" d="M6.6 10.8a15.1 15.1 0 0 0 6.6 6.6l2.2-2.2c.3-.3.7-.4 1-.2 1.1.4 2.3.6 3.6.6.6 0 1 .4 1 1V20c0 .6-.4 1-1 1A17 17 0 0 1 3 4c0-.6.4-1 1-1h3.5c.6 0 1 .4 1 1 0 1.3.2 2.5.6 3.6.1.3 0 .7-.2 1z"/></svg>
        07000 - 123 45 67
      </div>
      <div class="contact__address">Lindenweg 12<br>70000 Musterstadt</div>
    </div>

    <div class="footer-link">info@rohrreinigung-krw.de</div>
  </section>

  <div class="side-label side-label--back">Rückseite</div>

  <section class="card card--back" aria-label="Visitenkarte Rückseite">
    <svg class="card__bg" viewBox="0 0 460 295" width="460" height="295" aria-hidden="true">
      <polygon points="0,0 236,0 290,295 0,295" fill="var(--blue)"/>
      <rect x="0" y="242" width="460" height="53" fill="var(--navy)"/>
      <path d="M0,214 H184 a33,33 0 0 1 0,66 H0 Z" fill="var(--red)"/>
    </svg>

    <ul class="services">
      <li>grabenlose Kanalsanierung</li>
      <li>TV-Kamerainspektion</li>
      <li>Dichtheitsprüfung DIN EN 1610</li>
      <li>Fräsarbeiten mit Roboter</li>
      <li>Fräsarbeiten mit<br>Wasserhöchstdruck 2.500 Bar</li>
      <li>Verstopfungsbeseitigung</li>
    </ul>

    <div class="hotline">24H NOTDIENST<br>Tag &amp; Nacht<br>0150 - 000 111 22</div>
    <svg class="hotline__icon" style="left:158px;top:220px" width="52" height="54" viewBox="0 0 52 54" aria-hidden="true">
      <circle cx="30" cy="22" r="17" fill="none" stroke="#fff" stroke-width="3"/>
      <path d="M30 12 V22 L37 27" fill="none" stroke="#fff" stroke-width="3" stroke-linecap="round"/>
      <rect x="2" y="36" width="24" height="12" rx="2" fill="#fff"/>
      <circle cx="8" cy="50" r="3" fill="#fff"/><circle cx="21" cy="50" r="3" fill="#fff"/>
    </svg>

    <div class="callout">
      <p>Abfluss oder<br>Rohr verstopft?</p>
      <p>Jetzt anrufen,<br>wir kommen<br>sofort!</p>
    </div>

    <div class="footer-link">www.rohrreinigung-krw.de</div>
  </section>
</body>
</html>
```